physical therapy flyer

2 office locations speciality programs - work injury / Motor vehicle accidents - spanish speaking - do not put balance defecits/ fall prevention - Spanish speaking
neck and back pain shoulder pain/ rotator cuff disorder / bursitis
hip pain knee andle and foot pain post operative care including Spine , shoulder , knee , total joint replacement

Meadowline Physical therapy & Chiropractic
4827 Larchmont BLvd
kelso park ny 11592
7185521847
3719 Bexley Parkway
Bronx NY 11592
7189024613
www.meadowlineptclinic.com

```html
<!DOCTYPE html>
<html lang="en">
<head>
<meta charset="utf-8">
<title>Meadowline Physical Therapy Flyer</title>
<link href="https://fonts.googleapis.com/css2?family=Poppins:wght@400;500;600;700&display=swap" rel="stylesheet">
<style>
  :root{
    --green-dark:#1b7d39;
    --green-mid:#4fa53c;
    --green-light:#7cbc47;
    --green-pale:#eef6e7;
    --ink:#444444;
    --ink-soft:#5e5e5e;
    --pill:#3a3a3a;
    --white:#ffffff;
    --backdrop:#e6e6e6;
  }
  *{margin:0;padding:0;box-sizing:border-box}
  html,body{width:1200px;height:1200px;overflow:hidden;background:var(--backdrop)}
  body{position:relative;font-family:"Poppins",sans-serif}
  .flyer{
    position:absolute;left:152px;top:20px;
    width:1195px;height:1546px;
    transform:scale(0.75);transform-origin:top left;
    background:var(--white);overflow:hidden;
  }
  .abs{position:absolute}
  .hero-photo{left:520px;top:0;width:675px;height:470px;
    background:linear-gradient(180deg,#e9e6e3 0%,#f1efed 55%,#ffffff 100%)}
  .brand{left:50px;top:70px;display:flex;align-items:center;gap:16px}
  .brand-dot{width:56px;height:56px;border-radius:50%;background:var(--ink-soft)}
  .brand-name{font-size:27px;line-height:32px;color:var(--ink-soft);font-weight:400}
  .offer{left:32px;top:196px;width:612px;height:446px;
    background:linear-gradient(135deg,#72b642 0%,#84c24e 100%);
    border-radius:90px 0 140px 0;color:var(--white);padding:70px 0 0 55px}
  .offer-title{font-size:50px;font-weight:700;line-height:66px;letter-spacing:-0.3px}
  .offer-sub{font-size:32px;font-weight:400;line-height:41px;margin-top:8px}
  .tagline{left:692px;top:422px}
  .tagline-title{font-size:48px;font-weight:700;line-height:60px;color:var(--green-dark)}
  .tagline-sub{font-size:28px;line-height:36px;color:var(--ink);margin-top:4px}
  .conditions{left:40px;top:685px;width:1115px;height:220px}
  .condition{position:absolute;top:0;text-align:center;font-size:29px;font-weight:500;line-height:37px;color:var(--ink)}
  .condition svg{display:block;margin:0 auto 10px}
  .divider{position:absolute;top:5px;height:165px;border-left:3px dotted var(--green-mid)}
  .pale-band{left:0;top:0}
  .care-title{left:0;top:950px;width:1215px;text-align:center;font-size:42px;font-weight:700;line-height:53px;
    background:linear-gradient(90deg,var(--green-dark) 35%,var(--green-light) 100%);
    -webkit-background-clip:text;background-clip:text;color:transparent}
  .program{position:absolute;top:1083px;width:255px;text-align:center;font-size:23px;font-weight:700;line-height:30px;color:var(--ink-soft)}
  .program-photo{height:176px;border-radius:12px;margin-bottom:14px}
  .web-pill{left:54px;top:1336px;width:531px;height:64px;border-radius:32px;background:var(--pill);
    display:flex;align-items:center;gap:12px;padding-left:32px;color:var(--white);font-size:29px;font-weight:600;z-index:2}
  .footer-name{left:69px;top:1418px;font-size:28px;font-weight:700;line-height:33px;color:var(--white)}
  .office{top:1422px;color:var(--white);font-size:23px;line-height:29px;font-weight:400}
  .office-line{display:flex;gap:12px;align-items:flex-start}
  .office-phone{display:flex;gap:12px;align-items:center;font-size:27px;font-weight:700;margin-top:12px}
</style>
</head>
<body>
<div class="flyer">
  <div class="abs hero-photo" role="img" aria-label="Photo of a clinician holding a spine model while talking with a patient"></div>

  <div class="abs brand">
    <span class="brand-dot"></span>
    <span class="brand-name">Meadowline Physical Therapy,<br>Chiropractic, and Acupuncture</span>
  </div>

  <div class="abs offer">
    <div class="offer-title">Lesiones laborales<br>/ Accidentes<br>automovilísticos</div>
    <div class="offer-sub">No ponga déficit de<br>equilibrio/prevención<br>de caídas</div>
  </div>

  <div class="abs tagline">
    <div class="tagline-title">We Create<br>Healthy Families</div>
    <div class="tagline-sub">Call or Make an<br>Appointment Online Today.</div>
  </div>

  <svg class="abs pale-band" width="1195" height="1546" viewBox="0 0 1195 1546">
    <path d="M0 925 H1040 Q1170 925 1195 830 V1546 H0 Z" fill="var(--green-pale)"/>
    <path d="M0 1361 H1010 Q1180 1361 1195 1500 V1546 H0 Z" fill="url(#footGrad)"/>
    <defs>
      <linearGradient id="footGrad" x1="0" x2="1" y1="0" y2="0">
        <stop offset="0" stop-color="#6dba45"/>
        <stop offset="0.55" stop-color="#3b9a3f"/>
        <stop offset="1" stop-color="#177a37"/>
      </linearGradient>
    </defs>
  </svg>

  <div class="abs conditions">
    <div class="condition" style="left:20px;width:255px">
      <svg width="130" height="130" viewBox="0 0 130 130" role="img" aria-label="Neck and back pain icon">
        <circle cx="65" cy="65" r="60" fill="none" stroke="var(--green-mid)" stroke-width="4"/>
        <circle cx="65" cy="65" r="44" fill="#f1f1f1"/>
      </svg>Neck and Back<br>pain
    </div>
    <span class="divider" style="left:300px"></span>
    <div class="condition" style="left:335px;width:280px">
      <svg width="130" height="130" viewBox="0 0 130 130" role="img" aria-label="Shoulder pain icon">
        <circle cx="65" cy="65" r="60" fill="none" stroke="var(--green-mid)" stroke-width="4"/>
        <circle cx="65" cy="65" r="44" fill="#f1f1f1"/>
      </svg>Shoulder pain
    </div>
    <span class="divider" style="left:595px"></span>
    <div class="condition" style="left:625px;width:280px">
      <svg width="130" height="130" viewBox="0 0 130 130" role="img" aria-label="Rotator cuff disorder icon">
        <circle cx="65" cy="65" r="60" fill="none" stroke="var(--green-mid)" stroke-width="4"/>
        <circle cx="65" cy="65" r="44" fill="#f1f1f1"/>
      </svg>Rotator Cuff<br>disorder
    </div>
    <span class="divider" style="left:872px"></span>
    <div class="condition" style="left:900px;width:165px">
      <svg width="130" height="130" viewBox="0 0 130 130" role="img" aria-label="Bursitis knee joint icon">
        <circle cx="65" cy="65" r="60" fill="none" stroke="var(--green-mid)" stroke-width="4"/>
        <circle cx="65" cy="65" r="44" fill="#f1f1f1"/>
      </svg>Bursitis
    </div>
  </div>

  <div class="abs care-title">Hip pain knee handle and foot pain post<br>operative care including</div>

  <div class="program" style="left:73px">
    <div class="program-photo" role="img" aria-label="Photo of a therapist treating a patient's lower back" style="background:linear-gradient(135deg,#9aa3ab,#4f5e6b)"></div>Spine
  </div>
  <div class="program" style="left:341px">
    <div class="program-photo" role="img" aria-label="Photo of a therapist stretching a woman's shoulder" style="background:linear-gradient(135deg,#e6e2de,#b8c9a0)"></div>Shoulder
  </div>
  <div class="program" style="left:609px">
    <div class="program-photo" role="img" aria-label="Photo of a tennis player holding her injured knee" style="background:linear-gradient(135deg,#6f7a6a,#3b4a40)"></div>Knee
  </div>
  <div class="program" style="left:877px">
    <div class="program-photo" role="img" aria-label="Photo of a therapist supporting a patient's leg after joint replacement" style="background:linear-gradient(135deg,#ece8e4,#c9a48d)"></div>Total joint<br>replacement
  </div>

  <div class="abs web-pill">
    <svg width="28" height="28" viewBox="0 0 28 28" fill="none" stroke="var(--green-light)" stroke-width="2">
      <circle cx="14" cy="14" r="12"/><ellipse cx="14" cy="14" rx="5" ry="12"/><path d="M2 14H26M4 8H24M4 20H24"/>
    </svg>www.meadowlineptclinic.com
  </div>

  <div class="abs footer-name">Meadowline Physical<br>therapy &amp; Chiropractic</div>

  <div class="abs office" style="left:464px">
    <div class="office-line">
      <svg width="22" height="28" viewBox="0 0 22 28"><path d="M11 1C5.5 1 1 5.3 1 10.6 1 18 11 27 11 27S21 18 21 10.6C21 5.3 16.5 1 11 1Z" fill="none" stroke="#fff" stroke-width="2.5"/><circle cx="11" cy="10.5" r="3.5" fill="#fff"/></svg>
      <span>4827 Larchmont BLvd<br>kelso park ny 11592</span>
    </div>
    <div class="office-phone">
      <svg width="22" height="24" viewBox="0 0 24 24"><path d="M6.6 10.8a15 15 0 0 0 6.6 6.6l2.2-2.2c.3-.3.7-.4 1-.2 1.1.4 2.3.6 3.6.6.6 0 1 .4 1 1V20c0 .6-.4 1-1 1A17 17 0 0 1 3 4c0-.6.4-1 1-1h3.5c.6 0 1 .4 1 1 0 1.3.2 2.5.6 3.6.1.3 0 .7-.2 1z" fill="#fff"/></svg>
      <span>7185521847</span>
    </div>
  </div>

  <div class="abs office" style="left:800px">
    <div class="office-line">
      <svg width="22" height="28" viewBox="0 0 22 28"><path d="M11 1C5.5 1 1 5.3 1 10.6 1 18 11 27 11 27S21 18 21 10.6C21 5.3 16.5 1 11 1Z" fill="none" stroke="#fff" stroke-width="2.5"/><circle cx="11" cy="10.5" r="3.5" fill="#fff"/></svg>
      <span>3719 Bexley Parkway<br>Bronx NY 11592</span>
    </div>
    <div class="office-phone">
      <svg width="22" height="24" viewBox="0 0 24 24"><path d="M6.6 10.8a15 15 0 0 0 6.6 6.6l2.2-2.2c.3-.3.7-.4 1-.2 1.1.4 2.3.6 3.6.6.6 0 1 .4 1 1V20c0 .6-.4 1-1 1A17 17 0 0 1 3 4c0-.6.4-1 1-1h3.5c.6 0 1 .4 1 1 0 1.3.2 2.5.6 3.6.1.3 0 .7-.2 1z" fill="#fff"/></svg>
      <span>7189024613</span>
    </div>
  </div>
</div>
</body>
</html>
```